Flyer-Design
Zielgruppe
Ich bin gelernte Bankkauffrau, Dipl. Betriebswirtin, geprüfte Immobilienberaterin sowie Bausachverständige für Immobilienbewertung. Nach mehr als 30 Jahren Tätigkeit als Immobilienmaklerin für diverse Banken und große Maklerunternehmen, habe ich zum 01.01.2022 meine eigene Firma, die Tarvo Immobilienberatung GmbH & Co. KG gegründet.
Da Großunternehmen sehr unflexibel und träge sind und man dadurch nicht auf alle Bedürfnisse des Kunden so eingehen kann, wie ich es mir für meine Kunden wünsche, habe ich meine eigene Firma gegründet. Überschaubar groß, flexibel und Kundennah. Bei uns steht der Mensch mit all seinen Emotionen rund um den Immobilienverkauf im Vordergrund.
Wir bieten zusätzlich zum klassischen rundum-sorglos Immobilienverkauf von Bestandsimmobilien, auch Honorarberatung für Immobilien Selbstverkäufer an. Darüber hinaus auch Baufinanzierungen.
Unsere Zielgruppe sind verkaufsbereite Immobilieneigentümer jeglichen Alters. Meistens sind die Verkäufer jedoch im fortgeschrittenen Alter. Sowie Immobilienkäufer, die eine Finanzierung benötigen.
Aufgabenstellung
Er soll zum Design unserer Homepage passen www.tarvo-immobilien-beispiel.de.
Die Flyer sollen zum Auslegen, zur Mitnahme aus Hängeboxen und zum Briefkasteneinwurf dienen, um unsere Firma bekannt zu machen und Aufträge zu generieren.
Modern, aber nicht zu flippig/unruhig. Er muss die ältere Generation mit Bild und Text emotional ansprechen und Sicherheit vermitteln, aber auch die 30-40 Jährigen. Er soll sich von den üblichen, langweiligen Maklerflyern abheben.
Den Flyer wünschen wir uns später auch in DIN A4 Format zur Übergabe beim Kunden in einer Mappe.

```html
<!DOCTYPE html>
<html lang="de">
<head>
<meta charset="utf-8">
<title>Tarvo Immobilienberatung – Flyer</title>
<link href="https://fonts.googleapis.com/css2?family=Montserrat:wght@300;400;500;600;700;800&display=swap" rel="stylesheet">
<style>
  :root{
    --navy:#2a2d5c;
    --tan:#b99b76;
    --panel-top:rgba(120,82,48,.86);
    --panel-bottom:rgba(196,164,124,.94);
    --white:#ffffff;
  }
  *{margin:0;padding:0;box-sizing:border-box}
  html,body{width:857px;height:1200px;overflow:hidden;background:#fff}
  body{font-family:'Montserrat',sans-serif;color:var(--navy)}
  .flyer{position:relative;width:857px;height:1200px;overflow:hidden;background:var(--white)}

  .photo-room{position:absolute;left:0;top:0;width:857px;height:1012px;
    background:
      radial-gradient(ellipse 260px 200px at 620px 420px,rgba(246,238,224,.9),rgba(246,238,224,0) 70%),
      radial-gradient(ellipse 160px 260px at 800px 330px,rgba(40,44,52,.75),rgba(40,44,52,0) 75%),
      radial-gradient(ellipse 120px 90px at 780px 300px,rgba(214,110,70,.55),rgba(214,110,70,0) 75%),
      radial-gradient(ellipse 260px 120px at 600px 560px,rgba(92,62,40,.55),rgba(92,62,40,0) 75%),
      linear-gradient(180deg,#55524f 0%,#8c857c 18%,#d6cdbf 42%,#cbbfae 62%,#a89886 100%)}
  .photo-tablet{position:absolute;left:0;top:330px;width:430px;height:682px;
    background:
      radial-gradient(ellipse 200px 240px at 120px 220px,rgba(214,222,232,.55),rgba(214,222,232,0) 70%),
      linear-gradient(160deg,#6a768a 0%,#404a5c 55%,#262c38 100%)}

  .shapes{position:absolute;left:0;top:0}

  .brand{position:absolute;left:92px;top:140px;color:var(--white)}
  .brand-name{font-size:54px;font-weight:700;letter-spacing:2px;line-height:1}
  .brand-sub{font-size:14px;font-weight:300;letter-spacing:2px;margin-top:14px;padding-bottom:8px;border-bottom:1px solid rgba(255,255,255,.6);width:220px}

  .claim{position:absolute;left:92px;top:522px;line-height:1.05;color:var(--navy)}
  .claim .light{font-size:34px;font-weight:400;display:block}
  .claim .bold{font-size:40px;font-weight:800;display:block}

  .intro{position:absolute;left:92px;top:758px;width:255px;font-size:12.5px;font-weight:500;line-height:1.45;color:var(--white);text-shadow:0 1px 2px rgba(60,40,20,.45)}

  .logo{position:absolute;left:560px;top:22px;width:240px;height:58px;background:var(--white);display:flex;align-items:center;gap:10px;padding:0 14px}
  .logo-mark{width:22px;height:22px;background:var(--navy);flex:none}
  .logo-text{font-weight:800;font-size:26px;color:var(--navy);line-height:1}
  .logo-tag{font-size:8px;font-weight:800;color:var(--navy);margin-top:3px}

  .services-title{position:absolute;left:480px;top:712px;width:380px;text-align:center;font-size:36px;font-weight:800;line-height:1.2;color:var(--navy)}
  .services{list-style:none;position:absolute;top:818px;left:0;width:857px;font-size:19px;font-weight:500;color:var(--navy)}
  .services li{position:absolute;white-space:nowrap}
  .services li::before{content:"";display:inline-block;width:9px;height:9px;border-radius:50%;background:var(--tan);margin-right:7px;vertical-align:middle}

  .types{position:absolute;top:1026px;left:0;width:857px}
  .type{position:absolute;width:200px;text-align:center;font-size:13px;font-weight:500}
  .type svg{display:block;margin:0 auto 10px}

  .footer{position:absolute;left:0;top:1142px;width:857px;height:58px;background:var(--navy);color:var(--white);font-size:13px;font-weight:500}
  .contact{position:absolute;top:0;height:58px;display:flex;align-items:center;gap:14px}
</style>
</head>
<body>
<div class="flyer">
  <div class="photo-room" role="img" aria-label="Foto eines modernen Wohnraums mit hellem Sofa, Holztisch, Steinskulpturen und Blumen"></div>
  <div class="photo-tablet" role="img" aria-label="Foto eines Tablets mit Diagrammen auf einem Tisch"></div>

  <svg class="shapes" width="857" height="1200" viewBox="0 0 857 1200">
    <defs>
      <linearGradient id="panelFill" x1="0" y1="0" x2="0" y2="1">
        <stop offset="0" stop-color="var(--panel-top)"/>
        <stop offset="0.4" stop-color="var(--panel-top)"/>
        <stop offset="0.58" stop-color="var(--panel-bottom)"/>
        <stop offset="1" stop-color="var(--panel-bottom)"/>
      </linearGradient>
    </defs>
    <polygon points="60,0 372,0 372,814 60,980" fill="url(#panelFill)"/>
    <polygon points="857,556 857,1200 0,1200 0,1012" fill="var(--white)"/>
    <polygon points="372,814 857,556 857,530 372,788" fill="var(--tan)"/>
  </svg>

  <div class="brand">
    <div class="brand-name">TARVO</div>
    <div class="brand-sub">IMMOBILIENBERATUNG</div>
  </div>

  <div class="claim">
    <span class="light">IHR</span>
    <span class="bold">EXPERTE</span>
    <span class="light">IN IHRER</span>
    <span class="bold">REGION</span>
  </div>

  <p class="intro">Egal ob Sie Ihre Immobilie ohne Makler verkaufen oder sich lieber entspannt zurücklehnen wollen – bei uns sind Sie in jedem Fall richtig.</p>

  <div class="logo">
    <span class="logo-mark"></span>
    <div>
      <div class="logo-text">TARVO</div>
      <div class="logo-tag">Beratung mit Vertrauen</div>
    </div>
  </div>

  <h2 class="services-title">WAS WIR<br>FÜR SIE TUN</h2>
  <ul class="services">
    <li style="left:398px;top:0">Rundum-sorglos Immobilienverkauf</li>
    <li style="left:358px;top:27px">Honorarberatung für Immobilien Selbstverkäufer</li>
    <li style="left:338px;top:54px">Immobilienbewertung</li>
    <li style="left:294px;top:81px">Bonitätsprüfung</li>
    <li style="left:254px;top:108px">Finanzierungsvermittlung</li>
    <li style="left:218px;top:135px">Home Staging</li>
  </ul>

  <div class="types">
    <div class="type" style="left:41px">
      <svg width="44" height="40" viewBox="0 0 44 40" fill="none" stroke="var(--navy)" stroke-width="1.6"><path d="M4 20 22 5 40 20"/><path d="M9 16v20h26V16"/><rect x="18" y="24" width="8" height="12"/></svg>Haus</div>
    <div class="type" style="left:247px">
      <svg width="44" height="40" viewBox="0 0 44 40" fill="none" stroke="var(--navy)" stroke-width="1.6"><rect x="8" y="4" width="16" height="32"/><rect x="24" y="14" width="12" height="22"/><path d="M12 9h3M17 9h3M12 15h3M17 15h3M12 21h3M17 21h3M12 27h3M17 27h3M28 19h4M28 25h4"/></svg>Mehrfamilienhaus</div>
    <div class="type" style="left:451px">
      <svg width="44" height="40" viewBox="0 0 44 40" fill="none" stroke="var(--navy)" stroke-width="1.6"><path d="M4 34V10M40 34V22H4"/><rect x="8" y="15" width="8" height="7"/><path d="M18 22v-6h18a4 4 0 0 1 4 4v2"/></svg>Wohnung</div>
    <div class="type" style="left:654px">
      <svg width="44" height="40" viewBox="0 0 44 40" fill="none" stroke="var(--navy)" stroke-width="1.6"><path d="M6 36V10l3-4 3 4v26M16 36V10l3-4 3 4v26M26 36V10l3-4 3 4v26M36 36V10l3-4 3 4v26M2 16h40M2 28h40"/></svg>Grundstücksfläche</div>
  </div>

  <footer class="footer">
    <div class="contact" style="left:110px">
      <svg width="20" height="20" viewBox="0 0 24 24" fill="var(--white)"><path d="M6.6 10.8a15 15 0 0 0 6.6 6.6l2.2-2.2a1 1 0 0 1 1-.25 11.4 11.4 0 0 0 3.6.57 1 1 0 0 1 1 1V20a1 1 0 0 1-1 1A17 17 0 0 1 3 4a1 1 0 0 1 1-1h3.5a1 1 0 0 1 1 1c0 1.25.2 2.45.57 3.57a1 1 0 0 1-.25 1z"/></svg>
      <span>04 17 58 26 93</span>
    </div>
    <div class="contact" style="left:342px">
      <svg width="16" height="16" viewBox="0 0 16 16"><circle cx="8" cy="8" r="7" fill="var(--white)"/></svg>
      <span>Social Media</span>
    </div>
    <div class="contact" style="left:576px">
      <svg width="18" height="22" viewBox="0 0 24 30" fill="var(--white)"><path d="M12 0a11 11 0 0 0-11 11c0 8 11 19 11 19s11-11 11-19A11 11 0 0 0 12 0zm0 15a4 4 0 1 1 0-8 4 4 0 0 1 0 8z"/></svg>
      <span>Location</span>
    </div>
  </footer>
</div>
</body>
</html>
```